Flyer needed for a Summer Course

We need a flyer made for a summer course that will review a chapter of the Qur'an (holy book). The flyer can include imagery related to a table spread with delicious food outdoors in a garden setting, or any generic light/path to a garden or to light. Please include the attached logo to the flyer as well. The following information should be included in the flyer:
Tafsir of Surah Maidah
Taught by Delira Nasrim
June 1 to June 15 2017
Daily Monday thru Thursday
1:30 PM to 2:30 PM
Unity Hall of Brookvale Township
2400 Tarrow Road
Piscataway NJ 08617
For more information: sahelwing4@quorimail.com

```html
<!DOCTYPE html>
<html lang="en">
<head>
<meta charset="utf-8">
<title>Tafsir of Sura Maidah – Summer Course Flyer</title>
<link href="https://fonts.googleapis.com/css2?family=Anton&family=Roboto:wght@400;700&family=Raleway:wght@400&family=Yellowtail&family=Exo+2:wght@600&display=swap" rel="stylesheet">
<style>
  :root {
    --stage: #2b2b2d;
    --crimson: #b8174f;
    --crimson-deep: #7d0c33;
    --crimson-bright: #e02a6c;
    --glow: #f6d9e3;
    --accent: #f39a1e;
    --accent-warm: #ee6a1f;
    --ink: #ffffff;
    --ice: #cfe6f6;
    --ice-deep: #8ebfe0;
  }
  * { margin: 0; padding: 0; box-sizing: border-box; }
  html, body {
    width: 1200px; height: 1200px; overflow: hidden;
    background: var(--stage);
  }
  .flyer {
    position: absolute; left: 178px; top: 0;
    width: 844px; height: 1200px; overflow: hidden;
    background:
      radial-gradient(ellipse 360px 300px at 150px 230px, var(--glow) 0%, rgba(246,217,227,0.55) 35%, rgba(246,217,227,0) 75%),
      radial-gradient(ellipse 500px 420px at 420px 620px, rgba(240,60,120,0.55) 0%, rgba(240,60,120,0) 70%),
      radial-gradient(ellipse 700px 500px at 700px 160px, rgba(110,10,45,0.7) 0%, rgba(110,10,45,0) 70%),
      linear-gradient(180deg, var(--crimson) 0%, var(--crimson-bright) 48%, var(--crimson) 75%, var(--crimson-deep) 100%);
  }
  .art { position: absolute; }
  .art--hanging-lantern {
    left: 28px; top: 0; width: 142px; height: 271px;
    background: linear-gradient(180deg, #3a0a1c 0%, #5c1230 40%, #f3cbd8 70%, #3a0a1c 100%);
    border-radius: 40px 40px 20px 20px;
    opacity: 0.9;
  }
  .art--table-lantern {
    left: 547px; top: 747px; width: 297px; height: 453px;
    background:
      radial-gradient(ellipse 110px 170px at 170px 260px, #ffffff 0%, #f3d4df 40%, rgba(243,212,223,0) 80%),
      linear-gradient(160deg, #d0386f 0%, #8e1a44 55%, #f1c8d6 100%);
    border-radius: 90px 0 0 0;
  }
  .brand {
    position: absolute; left: 547px; top: 288px; width: 240px;
    text-align: center;
    font-family: "Exo 2", sans-serif; font-weight: 600;
    font-size: 27px; line-height: 1.1; color: var(--accent);
  }
  .title {
    position: absolute; left: 0; width: 844px; text-align: center;
    font-family: "Anton", sans-serif; text-transform: uppercase;
    line-height: 1; letter-spacing: -3px;
    text-shadow: 0 4px 0 #6a7f90, 0 8px 14px rgba(60,0,20,0.6);
  }
  .title--top { top: 418px; left: -38px; font-size: 128px; color: #f7f9fb; }
  .title--main { top: 526px; left: -22px; font-size: 132px; color: var(--ice); }
  .teacher {
    position: absolute; top: 640px; left: 0; width: 844px; text-align: center;
    padding-left: 50px;
    font-family: "Yellowtail", cursive; font-size: 54px; color: var(--ink);
    text-shadow: 0 2px 6px rgba(60,0,20,0.5);
  }
  .details { position: absolute; left: 45px; color: var(--ink); font-family: "Roboto", sans-serif; }
  .detail { position: absolute; left: 0; width: 560px; }
  .detail__icon { position: absolute; left: 0; width: 38px; height: 38px; }
  .detail__text { position: absolute; left: 49px; font-size: 24px; line-height: 30px; white-space: nowrap; }
  .detail__text strong { font-size: 36px; font-weight: 700; line-height: 40px; display: block; }
  .detail--date { top: 790px; }
  .detail--time { top: 870px; }
  .detail--place { top: 926px; }
  .detail--contact { top: 1034px; }
  .detail--contact .detail__text { font-family: "Raleway", sans-serif; font-size: 26px; line-height: 29px; }
</style>
</head>
<body>
  <main class="flyer">
    <div class="art art--hanging-lantern" role="img" aria-label="Ornate hanging lantern silhouette over a glowing geometric pattern"></div>
    <div class="art art--table-lantern" role="img" aria-label="Glowing carved lantern resting on draped fabric over a tiled floor"></div>

    <div class="brand">Ayat Learning Collective</div>

    <h1>
      <span class="title title--top">Tafsir of</span>
      <span class="title title--main">Sura Maidah</span>
    </h1>
    <p class="teacher">Taught by Delira Nasrim</p>

    <section class="details">
      <div class="detail detail--date">
        <svg class="detail__icon" viewBox="0 0 38 38" fill="none" stroke="var(--accent)" stroke-width="2.5">
          <rect x="3" y="7" width="32" height="28" rx="2"/>
          <line x1="3" y1="14" x2="35" y2="14"/>
          <line x1="11" y1="3" x2="11" y2="10"/><line x1="27" y1="3" x2="27" y2="10"/>
          <line x1="3" y1="21" x2="35" y2="21"/><line x1="3" y1="28" x2="35" y2="28"/>
          <line x1="11" y1="14" x2="11" y2="35"/><line x1="19" y1="14" x2="19" y2="35"/><line x1="27" y1="14" x2="27" y2="35"/>
        </svg>
        <p class="detail__text"><strong>June 1 to June 15 2017</strong>Daily Monday thru Thursday</p>
      </div>
      <div class="detail detail--time">
        <svg class="detail__icon" viewBox="0 0 38 38" fill="none" stroke="var(--accent)" stroke-width="2.5">
          <circle cx="19" cy="19" r="16"/>
          <path d="M19 10 V19 L25 23"/>
        </svg>
        <p class="detail__text" style="top:3px">1:30 PM to 2:30 PM</p>
      </div>
      <div class="detail detail--place">
        <svg class="detail__icon" viewBox="0 0 38 38" fill="none" stroke="var(--accent)" stroke-width="2.5" style="top:10px">
          <circle cx="19" cy="19" r="16"/>
          <path d="M10 19 L19 11 L28 19" />
          <path d="M13 18 V27 H25 V18" fill="var(--accent)"/>
        </svg>
        <p class="detail__text">Unity Hall of Brookvale Township<br>2400 Tarrow Road<br>Piscataway NJ 08617</p>
      </div>
      <div class="detail detail--contact">
        <svg class="detail__icon" viewBox="0 0 38 38" fill="none" stroke="var(--accent)" stroke-width="2.5" style="top:2px">
          <circle cx="19" cy="19" r="16"/>
          <rect x="10" y="13" width="18" height="12" rx="1"/>
          <path d="M10 14 L19 21 L28 14"/>
        </svg>
        <p class="detail__text">For more information:<br>sahelwing4@quorimail.com</p>
      </div>
    </section>
  </main>
</body>
</html>
```